WP website design (Pell)

We need a wordpress design for an established auction and real estate company based in Texas. The winning design will incorporate a professional color scheme with company logo in a clean layout. The design needs to consider that this will be developed on a responsive theme. Colors are those that will highlight the logo.
Updates

Reason: was waiting for updated logo

Industry/Entity Type

Real Estate

Font styles to use
Serif
Sans Serif

Requirements
Must have
• Navigation:
1) Home
2) Auctions
3) Online Auctions
4) Services
5) About Us
6) Contact us

Slideshow will be used - please use stock real estate photo. Tag line in the header - "Your Austin Auction Professionals!” Color of the site will be those in the logo and black.

Widgets - 1) Social media icons for zendly, plimora, vastoGrid and Rss. 2) News & events blog, 3) Featured video, 4) Email Sign-up, 5) Testimonials

Company logo and contact info in the footer with attached logos too.
Nice to have
• Use of a drop down menu style - under 'Auctions'
1) Upcoming Auctions
2) Past Auctions

```html
<!DOCTYPE html>
<html lang="en">
<head>
<meta charset="utf-8">
<title>Pell Brothers Auction Service</title>
<link href="https://fonts.googleapis.com/css2?family=Ubuntu:wght@400;500;700&family=Arimo:wght@400;700&display=swap" rel="stylesheet">
<style>
:root{
  --blue:#2d2f94;
  --blue-dark:#23257a;
  --red:#e3222a;
  --ink:#222;
  --page:#1c1c1c;
  --panel:#f2f2f2;
  --line:#d6d6d6;
  --white:#fff;
}
*{margin:0;padding:0;box-sizing:border-box}
html,body{width:878px;height:1200px;overflow:hidden}
body{background:var(--page);font-family:"Arimo",Arial,sans-serif;color:var(--ink);position:relative}
.abs{position:absolute}
.sheet{position:absolute;left:66px;top:14px;width:744px;height:1084px;background:var(--white);border-radius:6px}
/* nav */
.nav{position:absolute;left:73px;top:18px;width:731px;height:33px;background:var(--blue);border-radius:4px 4px 0 0}
.nav a{position:absolute;top:0;height:33px;line-height:33px;color:#fff;font-size:9.5px;font-weight:700;text-decoration:none;text-transform:uppercase;letter-spacing:.2px;transform:translateX(-50%);white-space:nowrap}
.nav .sep{position:absolute;top:4px;width:1px;height:29px;background:#4a4cab}
.nav .active{background:var(--red);width:76px;text-align:center;transform:none;height:27px;line-height:27px;top:4px}
.dropdown{position:absolute;left:132px;top:54px;width:116px;height:57px;background:var(--blue);z-index:5}
.dropdown span{display:block;height:23px;line-height:23px;padding-left:9px;color:#fff;font-size:11px;font-family:"Ubuntu",sans-serif}
.dropdown .current{background:var(--red)}
/* hero */
.hero-frame{position:absolute;left:232px;top:68px;width:570px;height:308px;border:1px solid var(--line)}
.hero{position:absolute;left:238px;top:72px;width:554px;height:294px;background:linear-gradient(180deg,#5d7fc2 0%,#a8bfe3 30%,#d8c7ae 50%,#b9703f 70%,#4c6b2a 85%,#7b7b74 100%)}
.tagline{position:absolute;left:288px;top:112px;width:504px;height:38px;background:rgba(40,40,70,.55);color:#fff;font-family:"Ubuntu",sans-serif;font-size:20px;line-height:38px;padding-left:40px}
.crest-clip{position:absolute;left:74px;top:60px;width:270px;height:320px;overflow:hidden}
.crest{position:absolute;left:-46px;top:12px;width:296px;height:296px;border-radius:50%;background:radial-gradient(circle at 50% 40%,#fff 55%,#e2e2e2 100%);border:4px solid #fff;box-shadow:0 0 0 1px var(--line)}
.brand{position:absolute;left:75px;top:134px;width:200px;text-align:center;font-family:"Ubuntu",sans-serif;font-weight:700;color:var(--blue);line-height:1}
.brand .l1{font-size:46px;display:block}
.brand .l2{font-size:37px;display:block;margin-top:2px}
.brand .l3{font-size:20px;display:block;margin-top:16px;letter-spacing:3px}
.brand .l4{font-size:16px;display:block;margin-top:6px;letter-spacing:4px}
.crest-rule{position:absolute;left:74px;top:301px;width:230px;height:1px;background:var(--line)}
.social{position:absolute;top:310px;width:29px;height:29px;border-radius:50%}
/* left widgets */
.signup{position:absolute;left:75px;top:398px;width:223px;height:114px;background:var(--blue);border-radius:5px;color:#fff;padding:12px 15px}
.signup h2{font-family:"Ubuntu",sans-serif;font-weight:400;font-size:21px}
.signup p{font-size:10.5px;line-height:13px;margin-top:8px}
.signup .field{position:absolute;left:15px;top:75px;width:145px;height:22px;background:#fff;color:#999;font-size:10px;line-height:22px;padding-left:5px}
.signup .go{position:absolute;left:160px;top:75px;width:49px;height:22px;background:var(--red);color:#fff;font-size:10.5px;font-weight:700;line-height:22px;text-align:center;border-radius:0 4px 4px 0}
.video{position:absolute;left:75px;top:532px;width:221px;height:149px;background:linear-gradient(135deg,#51703a 0%,#7e9b60 40%,#c9b9a3 65%,#2f3a2a 100%)}
.video .bar{position:absolute;left:0;bottom:0;width:221px;height:13px;background:#111}
.card-box{position:absolute;left:75px;width:223px;background:var(--panel);border:1px solid var(--line);border-radius:5px;padding:8px 10px}
.card-box h2{font-family:"Ubuntu",sans-serif;font-weight:400;font-size:22px;color:var(--red)}
.news ul{list-style:none;margin-top:10px}
.news li{font-size:9px;line-height:11.5px;color:#333;padding-left:12px;position:relative;margin-bottom:9px}
.news li::before{content:"»";position:absolute;left:1px;top:0;color:var(--blue);font-weight:700}
.quote{font-size:9.8px;line-height:14.6px;color:#333;margin-top:12px}
.quote .mk{font-family:"Ubuntu",sans-serif;font-size:15px;color:#666}
.author{text-align:right;margin-top:8px;font-family:"Ubuntu",sans-serif;font-weight:500;font-style:italic;font-size:10px;color:var(--blue);text-decoration:underline;padding-right:4px}
/* main */
.main-title{position:absolute;left:316px;font-family:"Ubuntu",sans-serif;font-weight:400;color:var(--blue);font-size:21px}
.intro{position:absolute;left:317px;top:430px;width:479px;font-size:9.9px;line-height:15.4px;text-align:justify;color:#333}
.lot{position:absolute;left:316px;width:486px;height:115px;background:var(--panel);border:1px solid var(--line);border-radius:5px}
.lot .thumb{position:absolute;left:8px;top:8px;width:92px;height:92px;background:#fff;border:1px solid var(--line);border-radius:3px;padding:5px}
.lot .thumb div{width:100%;height:100%;background:linear-gradient(135deg,#3f5d2c 0%,#7f9a60 45%,#e7e7e7 60%,#2e3b27 100%)}
.lot .info{position:absolute;left:110px;top:12px;font-size:9.6px;line-height:13px;color:#222}
.lot .info h3{font-family:"Arimo",sans-serif;font-weight:700;font-size:10.4px;color:var(--blue);margin-bottom:4px}
.lot .info .bold{font-weight:700;font-size:9px}
.lot .info .sp{margin-top:1px;font-size:10px}
.btn{position:absolute;left:382px;width:90px;height:25px;border-radius:3px;color:#fff;font-size:10.5px;font-weight:700;letter-spacing:.6px;line-height:25px;padding-left:30px;box-shadow:inset 0 -2px 0 rgba(0,0,0,.15)}
.btn svg{position:absolute;left:11px;top:6px}
.btn.details{top:23px;background:var(--red)}
.btn.gallery{top:65px;background:var(--blue)}
/* footer */
.contact{position:absolute;left:79px;top:1113px;color:#eee;font-size:10px;line-height:15px}
.foot-brand{position:absolute;left:482px;top:1124px;width:50px;text-align:center;font-family:"Ubuntu",sans-serif;font-weight:700;color:#9a9a9a;font-size:11px;line-height:11px}
.badge{position:absolute;background:#7d7d7d}
.copyright{position:absolute;left:0;top:1175px;width:878px;height:25px;background:var(--blue);color:#fff;font-size:9.5px;line-height:25px;text-align:center}
</style>
</head>
<body>
<div class="sheet"></div>

<nav class="nav">
  <a style="left:26px">Home</a>
  <span class="sep" style="left:61px"></span>
  <a class="active" style="left:61px">Auctions</a>
  <span class="sep" style="left:146px"></span>
  <a style="left:199px">Online Auctions</a>
  <span class="sep" style="left:255px"></span>
  <a style="left:298px">About Us</a>
  <span class="sep" style="left:339px"></span>
  <a style="left:377px">Services</a>
  <span class="sep" style="left:417px"></span>
  <a style="left:484px">Real Estate Listings</a>
  <span class="sep" style="left:550px"></span>
  <a style="left:597px">References</a>
  <span class="sep" style="left:646px"></span>
  <a style="left:690px">Contact Us</a>
</nav>

<div class="hero-frame"></div>
<div class="hero" role="img" aria-label="Stock photo of a stucco house with a red tile roof, garden and driveway under a blue sky"></div>
<div class="tagline">Your Austin Auction Professionals!</div>

<div class="crest-clip"><div class="crest"></div></div>
<div class="brand"><span class="l1">PELL</span><span class="l2">BROTHERS</span><span class="l3">AUCTION</span><span class="l4">SERVICE</span></div>
<div class="crest-rule"></div>
<span class="social" style="left:97px;background:#3d8fd8" role="img" aria-label="zendly"></span>
<span class="social" style="left:135px;background:#2d4a8f" role="img" aria-label="plimora"></span>
<span class="social" style="left:174px;background:#2a6fb0" role="img" aria-label="vastoGrid"></span>
<span class="social" style="left:210px;background:#ee9b22" role="img" aria-label="RSS feed"></span>

<div class="dropdown"><span>Upcoming Auctions</span><span class="current">Past Auctions</span></div>

<section class="signup">
  <h2>Email Sign Up</h2>
  <p>Sign up for our free messages &amp; receive auction alerts.</p>
  <div class="field">Email Address</div>
  <div class="go">Submit</div>
</section>

<div class="video" role="img" aria-label="Featured video still of two clients meeting an auctioneer beside a yard sign">
  <svg class="abs" style="left:89px;top:47px" width="44" height="44" viewBox="0 0 44 44"><circle cx="22" cy="22" r="20" fill="rgba(30,30,30,.8)" stroke="#ddd" stroke-width="2"/><path d="M17 12 L32 22 L17 32Z" fill="#ddd"/></svg>
  <div class="bar">
    <svg width="221" height="13"><path d="M7 3 L12 6.5 L7 10Z" fill="#fff"/><rect x="20" y="5.5" width="160" height="2" fill="#555"/><rect x="20" y="5.5" width="66" height="2" fill="#e3222a"/><rect x="191" y="4.5" width="5" height="4" fill="#ddd"/><rect x="205" y="3.5" width="8" height="6" fill="none" stroke="#ddd"/></svg>
  </div>
</div>

<section class="card-box news" style="top:699px;height:173px">
  <h2>News &amp; Event Blog</h2>
  <ul>
    <li>Great Land Auction Companies Make All the Difference</li>
    <li>Great OK Farms for Sale at Auction Prices</li>
    <li>Farmland Auctions on Route 66</li>
    <li>Great Land Auction Companies Make All the Difference</li>
    <li>Great OK Farms for Sale at Auction Prices</li>
  </ul>
</section>

<section class="card-box" style="top:891px;height:167px">
  <h2>Testimonials</h2>
  <p class="quote"><span class="mk">“</span> simply dummy text of the printing and typesetting industry. Lorem Ipsum has been the industry's standard dummy text ever since the 1500s, when an unknown printer took a galley of type and scrambled it to make a type specimen book. <span class="mk">”</span></p>
  <p class="author">Mira Castell</p>
</section>

<h1 class="main-title" style="top:397px">Welcome to Pell Brothers Auction Service</h1>
<p class="intro">simply dummy text of the printing and typesetting industry. Lorem Ipsum has been the industry's standard dummy text ever since the 1500s, when an unknown printer took a galley of type and scrambled it to make a type specimen book. It has survived not only five centuries, but also the leap into electronic typesetting, remaining essentially unchanged. It was popularised in the 1960s with the release of Corvane sheets containing Lorem Ipsum passages,</p>
<h2 class="main-title" style="top:527px">Upcoming Auction</h2>

<article class="lot" style="top:566px">
  <div class="thumb"><div role="img" aria-label="Auction listing photo of two men beside a company yard sign"></div></div>
  <div class="info"><h3>Auction and real estate company based in Texas</h3><div>FENWICK AREA * CROP &amp; TIMBER</div><div class="bold">160± ACRES LAND REDBANK COUNTY, OK ~ FENWICK</div><div class="sp">Begins:&nbsp; Tuesday, March 12, 2013 at 10:00 AM CDT</div><div class="sp"><b>Location:</b>&nbsp; See Directions</div><div>United States Fenwick, OK 74699</div></div>
  <div class="btn details"><svg width="14" height="14" viewBox="0 0 14 14"><circle cx="6" cy="6" r="4.2" fill="none" stroke="#fff" stroke-width="2"/><path d="M9 9 L13 13" stroke="#fff" stroke-width="2.4"/></svg>DETAILS</div>
  <div class="btn gallery"><svg width="16" height="13" viewBox="0 0 16 13"><rect x="1" y="1" width="14" height="11" fill="none" stroke="#fff" stroke-width="1.6"/><path d="M3 10 L7 5 L10 8 L12 6 L14 10Z" fill="#fff"/></svg>GALLERY</div>
</article>

<article class="lot" style="top:698px">
  <div class="thumb"><div role="img" aria-label="Auction listing photo of two men beside a company yard sign"></div></div>
  <div class="info"><h3>Auction and real estate company based in Texas</h3><div>FENWICK AREA * CROP &amp; TIMBER</div><div class="bold">160± ACRES LAND REDBANK COUNTY, OK ~ FENWICK</div><div class="sp">Begins:&nbsp; Tuesday, March 12, 2013 at 10:00 AM CDT</div><div class="sp"><b>Location:</b>&nbsp; See Directions</div><div>United States Fenwick, OK 74699</div></div>
  <div class="btn details"><svg width="14" height="14" viewBox="0 0 14 14"><circle cx="6" cy="6" r="4.2" fill="none" stroke="#fff" stroke-width="2"/><path d="M9 9 L13 13" stroke="#fff" stroke-width="2.4"/></svg>DETAILS</div>
  <div class="btn gallery"><svg width="16" height="13" viewBox="0 0 16 13"><rect x="1" y="1" width="14" height="11" fill="none" stroke="#fff" stroke-width="1.6"/><path d="M3 10 L7 5 L10 8 L12 6 L14 10Z" fill="#fff"/></svg>GALLERY</div>
</article>

<article class="lot" style="top:831px">
  <div class="thumb"><div role="img" aria-label="Auction listing photo of two men beside a company yard sign"></div></div>
  <div class="info"><h3>Auction and real estate company based in Texas</h3><div>FENWICK AREA * CROP &amp; TIMBER</div><div class="bold">160± ACRES LAND REDBANK COUNTY, OK ~ FENWICK</div><div class="sp">Begins:&nbsp; Tuesday, March 12, 2013 at 10:00 AM CDT</div><div class="sp"><b>Location:</b>&nbsp; See Directions</div><div>United States Fenwick, OK 74699</div></div>
  <div class="btn details"><svg width="14" height="14" viewBox="0 0 14 14"><circle cx="6" cy="6" r="4.2" fill="none" stroke="#fff" stroke-width="2"/><path d="M9 9 L13 13" stroke="#fff" stroke-width="2.4"/></svg>DETAILS</div>
  <div class="btn gallery"><svg width="16" height="13" viewBox="0 0 16 13"><rect x="1" y="1" width="14" height="11" fill="none" stroke="#fff" stroke-width="1.6"/><path d="M3 10 L7 5 L10 8 L12 6 L14 10Z" fill="#fff"/></svg>GALLERY</div>
</article>

<article class="lot" style="top:963px">
  <div class="thumb"><div role="img" aria-label="Auction listing photo of two men beside a company yard sign"></div></div>
  <div class="info"><h3>Auction and real estate company based in Texas</h3><div>FENWICK AREA * CROP &amp; TIMBER</div><div class="bold">160± ACRES LAND REDBANK COUNTY, OK ~ FENWICK</div><div class="sp">Begins:&nbsp; Tuesday, March 12, 2013 at 10:00 AM CDT</div><div class="sp"><b>Location:</b>&nbsp; See Directions</div><div>United States Fenwick, OK 74699</div></div>
  <div class="btn details"><svg width="14" height="14" viewBox="0 0 14 14"><circle cx="6" cy="6" r="4.2" fill="none" stroke="#fff" stroke-width="2"/><path d="M9 9 L13 13" stroke="#fff" stroke-width="2.4"/></svg>DETAILS</div>
  <div class="btn gallery"><svg width="16" height="13" viewBox="0 0 16 13"><rect x="1" y="1" width="14" height="11" fill="none" stroke="#fff" stroke-width="1.6"/><path d="M3 10 L7 5 L10 8 L12 6 L14 10Z" fill="#fff"/></svg>GALLERY</div>
</article>

<footer>
  <div class="contact">Office: (555) 310-2874<br>Fax: (555) 310-2875, Email:team@pellbros.example<br>Address: 118 W. Orchard Ave., Lindale KS</div>
  <div class="foot-brand">PELL<br>BROTHERS</div>
  <div class="badge" style="left:547px;top:1124px;width:143px;height:30px;border-radius:3px" role="img" aria-label="Partner university badge"></div>
  <div class="badge" style="left:705px;top:1118px;width:42px;height:42px;border-radius:50%" role="img" aria-label="Association seal"></div>
  <div class="badge" style="left:765px;top:1118px;width:36px;height:40px;border-radius:3px" role="img" aria-label="Auctioneer association badge"></div>
  <div class="copyright">Copyright © 2014 • Pell Brothers Auction Service • All Rights Reserved.</div>
</footer>
</body>
</html>
```